Wordpress Theme for Harbourline Clinics

** Please view updated Sitemap2.pdf doc to clarify some confusion ***

This is a multiuser WordPress subscription site for Harbourline Clinics. Please see attachment for sitemap. Please do not include extra content like social media icons, search bars, or images. If you have questions, please ask for clarification.
The site contains the following pages and sub-pages:

1. Home
2. Our Clinic
2a. Our Clinic > Mission
2b. Our Clinic > Services
2c. Our Clinic > Clinic Policies
2d. Our Clinic > Schedules
3. Our Staff
3a. Our Staff > [Staff member page]
4. Resources
4a. Resources > Patient Health (index)
4b. Resources > Patient Health (index) > [post]
4c. Resources > Links
4d. Resources > Forms
5. Alerts
5a. Alerts > [Alert Page]
6. Contact Us

Includes the Following Pages, Subpages, and Content
1. Home
a. About Us
b. Our Staff
c. Bulletins
d. Accepting New Patients (shown as an alert widget)
e. Links
i. Physician Toolbox
ii. Book an Appointment
f. Clinic Policies
i. Show first 3 policies (e.g. Late Arrivals, Missed Appointments, Fees)
ii. Link to Clinic Policies page
g. Primary widget (displayed on all pages)
i. Hours of operation
ii. Contact Info
1. Tel
2. Fax
3. Email
4. Address
5. Get directions (link to Google Maps)
2. Our Clinic
a. Main Page
i. Clinic Name
ii. Overview
iii. Languages Spoken
iv. Secondary Navigation
1. Mission
2. Services
3. Clinic Policies
4. Schedules (see attachment)
b. Our Clinic > Mission
c. Our Clinic > Services
i. For each service include service TITLE and DESCRIPTION
d. Our Clinic > Clinic Policies
i. For each policy include policy TITLE and DESCRIPTION
ii. Include the following policies in mockup
1. Late arrivals
2. Missed appointments
3. Fees for missed appointments
4. Referrals and follow-ups
5. Services not covered by RDV
6. Information for TQL patients
7. Medical Legal Reports
e. Our Clinic > Schedules
3. Our Staff
a. Main Page
i. Display a list of staff members. Include NAME and DESIGNATION
b. Our Staff > [Staff Name]
i. Include NAME, PICTURE, DESIGNATION, and BIO
4. Resources
a. Resources > Patient Health
i. Main Page
1. Posts (ordered by date)
a. Title
b. Summary
2. Side Navigation
a. Post Categories
ii. Patient Health > [post title]
1. Title
2. Post Category
3. Date
4. Author
5. Summary
6. Body
b. Resources > Links
1. Secondary Navigation - Categories
a. Sample Categories:
i. Local Services
ii. RDV and Drug Coverage
iii. Mental Health Resources
2. Category page
a. Include the following links in the 'Local Services' category
i. Hypertension clinics
ii. Home Care services
iii. Vaccine Clinics
c. Resources > Forms
i. Display a table with form TITLE and CATEGORY
ii. Side Navigation
1. Form Categories
a. Use the following sample Categories
i. Referrals
ii. Insurance
iii. Intake
iv. Discharge
v. Waivers
5. Alerts
a. Main page
i. List of all Alert posts
1. Include post TITLE as a link to the post
ii. Side Navigation
1. Alerts Archive
a. shown as Month + Number of posts
iii. Alerts > [Alert page]
1. Include TITLE, DATE, AUTHOR, BODY
6. Contact Us
a. Map
b. Hours of operation
c. Address
d. Phone number
e. Fax number
e. Fax number
f. Map
g. Email

Design notes:
- fixed width
- responsive (need designs for mobile, tablet, and desktop)
- simple, dark font, white background
- use Font Awesome icons where needed
- user adds own logo

Target Market(s)

Harbourline Clinics

Industry/Entity Type

Medical

Number of Pages Required

5+ page

Font styles to use
Serif
Sans Serif

Requirements
Must have
• Please keep designs very simple.
• Examples:
• https://www.quandrix.com/install
• http://www.tervolane.com/company/about-us
• http://brightnumberhub.org/
• http://www.vorn.com/
Should not have
• Minimal or no use of shadows and gradients

```html
<!DOCTYPE html>
<html lang="en">
<head>
<meta charset="utf-8">
<title>Harbourline Clinics – Our Clinic</title>
<link href="https://fonts.googleapis.com/css2?family=Open+Sans:wght@400;600;700&family=Raleway:wght@500&display=swap" rel="stylesheet">
<style>
  :root {
    --teal: #1cb8c8;
    --ink: #333a40;
    --text: #4a4a4a;
    --card: #e9e9e9;
    --button: #4a4a4a;
    --hero: #e4f0f5;
    --band: #e3e3e3;
    --footer: #1c1f2b;
    --footer-base: #111219;
    --footer-text: #c9ccd3;
    --lime: #9acd32;
    --white: #ffffff;
    --line: #d6d6d6;
  }
  * { margin: 0; padding: 0; box-sizing: border-box; }
  html, body { width: 1020px; height: 1200px; overflow: hidden; background: var(--white); }
  body { position: relative; font-family: Arial, Helvetica, sans-serif; color: var(--text); }
  .abs { position: absolute; }
  a { text-decoration: none; }

  .top-rule { left: 0; top: 0; width: 1020px; height: 2px; background: var(--teal); }
  .brand { left: 83px; top: 30px; font-family: "Open Sans", sans-serif; font-size: 29px; color: var(--ink); letter-spacing: -0.5px; }
  .header-contact { right: 85px; top: 44px; font-family: "Open Sans", sans-serif; font-weight: 600; font-size: 11.5px; color: var(--ink); display: flex; gap: 10px; align-items: center; }
  .header-contact span { display: flex; align-items: center; gap: 4px; }

  .main-nav { left: 0; top: 96px; width: 1020px; height: 42px; background: var(--teal); }
  .main-nav a { position: absolute; top: 0; height: 42px; line-height: 42px; color: var(--white); font-family: "Open Sans", sans-serif; font-weight: 600; font-size: 10px; text-transform: uppercase; transform: translateX(-50%); }
  .main-nav a.active { left: 167px; width: 88px; transform: none; text-align: center; background: var(--button); }
  .home-icon { left: 98px; top: 13px; }

  .hero { left: 0; top: 138px; width: 1020px; height: 187px; background: var(--hero); }
  .hero-title { left: 0; width: 1020px; top: 180px; text-align: center; font-family: "Open Sans", sans-serif; font-weight: 400; font-size: 24px; color: var(--ink); }
  .hero-sub { left: 0; width: 1020px; top: 216px; text-align: center; font-size: 14px; color: var(--ink); }

  .clinic-card { left: 84px; width: 851px; height: 190px; background: var(--card); }
  .card-side { position: absolute; left: 21px; top: 22px; width: 200px; height: 145px; background: var(--white); border: 1px solid var(--line); }
  .side-title { height: 29px; line-height: 28px; padding-left: 14px; background: var(--teal); color: var(--white); font-family: "Open Sans", sans-serif; font-weight: 700; font-size: 10.5px; letter-spacing: 0.5px; }
  .sub-nav a { display: block; height: 28.5px; line-height: 28px; padding-left: 14px; border-top: 1px solid var(--line); font-family: "Open Sans", sans-serif; font-size: 11.5px; color: var(--ink); }
  .sub-nav a::before { content: "›"; color: var(--teal); font-weight: 700; margin-right: 8px; }
  .languages { display: grid; grid-template-columns: 1fr 1fr; gap: 8px; padding: 12px 12px; }
  .languages span { height: 24px; line-height: 22px; border: 1px solid var(--line); text-align: center; font-family: "Open Sans", sans-serif; font-size: 11px; color: var(--ink); }
  .clinic-card h2 { position: absolute; left: 239px; top: 30px; font-family: "Open Sans", sans-serif; font-weight: 400; font-size: 20px; color: var(--ink); }
  .clinic-card p { position: absolute; left: 239px; top: 64px; width: 592px; font-size: 11.2px; line-height: 18px; color: var(--text); }
  .learn-more { position: absolute; left: 239px; top: 137px; width: 144px; height: 30px; line-height: 30px; background: var(--button); color: var(--white); text-align: center; font-family: "Open Sans", sans-serif; font-weight: 700; font-size: 11.5px; letter-spacing: 0.5px; }

  .hours-band { left: 0; top: 705px; width: 1020px; height: 193px; background: var(--band); }
  .hours-band h3 { position: absolute; left: 0; width: 1020px; top: 50px; text-align: center; font-family: "Open Sans", sans-serif; font-weight: 400; font-size: 23px; color: var(--ink); }
  .hours-field { position: absolute; left: 276px; top: 106px; width: 360px; height: 30px; background: var(--white); font-size: 11px; color: var(--text); line-height: 30px; padding-left: 16px; white-space: nowrap; }
  .directions { position: absolute; left: 636px; top: 106px; width: 132px; height: 30px; background: var(--teal); color: var(--white); text-align: center; line-height: 30px; font-family: "Open Sans", sans-serif; font-weight: 700; font-size: 11.5px; }

  .site-footer { left: 0; top: 898px; width: 1020px; height: 242px; background: var(--footer); }
  .footer-col { position: absolute; top: 30px; }
  .footer-col h4 { font-family: "Raleway", sans-serif; font-weight: 500; font-size: 19px; color: var(--white); }
  .footer-col h4 b { font-weight: 500; color: var(--teal); }
  .footer-col .rule { width: 55px; height: 2px; background: var(--teal); margin: 4px 0 12px; }
  .footer-col p { font-size: 10.5px; line-height: 18px; color: var(--footer-text); }
  .tagline { color: var(--lime) !important; font-weight: 700; font-size: 12px !important; margin-bottom: 2px; }
  .footer-links a { display: block; font-size: 10.5px; line-height: 24px; color: var(--teal); }
  .footer-links a::before { content: "›"; font-weight: 700; margin-right: 8px; }

  .footer-base { left: 0; top: 1140px; width: 1020px; height: 60px; background: var(--footer-base); }
  .footer-base p { position: absolute; left: 84px; top: 24px; font-size: 10px; color: var(--footer-text); }
</style>
</head>
<body>
  <div class="abs top-rule"></div>
  <div class="abs brand">Harbourline Clinics</div>
  <div class="abs header-contact">
    <span>
      <svg width="9" height="11" viewBox="0 0 9 11"><path d="M3 1 C1 2 1 9 3 10 L4 8 C3 7 3 4 4 3 Z" fill="#1cb8c8"/></svg>1234-555-019
    </span>
    <span>
      <svg width="11" height="9" viewBox="0 0 11 9"><rect width="11" height="9" rx="1" fill="#1cb8c8"/><path d="M0.5 1 L5.5 5 L10.5 1" stroke="#fff" fill="none"/></svg>hello@harbourline.example
    </span>
  </div>

  <nav class="abs main-nav">
    <svg class="abs home-icon" width="15" height="14" viewBox="0 0 15 14"><path d="M7.5 0 L15 7 H13 V14 H9 V9.5 H6 V14 H2 V7 H0 Z" fill="#fff"/></svg>
    <a class="active" href="#">Clinic</a>
    <a href="#" style="left:327px">Our Staff</a>
    <a href="#" style="left:457px">Resources</a>
    <a href="#" style="left:595px">Contact Us</a>
    <a href="#" style="left:733px">Log In</a>
    <a href="#" style="left:835px">Sign Up</a>
  </nav>

  <section class="abs hero"></section>
  <h1 class="abs hero-title">CLINIC</h1>
  <p class="abs hero-sub">Donec vestibulum justo a diam ultricies pellentesque. Quisque mattis</p>

  <article class="abs clinic-card" style="top:273px">
    <div class="card-side">
      <div class="side-title">OUR CLINIC</div>
      <nav class="sub-nav">
        <a href="#">Mission</a>
        <a href="#">Services</a>
        <a href="#">Clinic Policies</a>
        <a href="#">Schedules</a>
      </nav>
    </div>
    <h2>Harbourline Clinic</h2>
    <p>Donec vestibulum justo a diam ultricies pellentesque. Quisque mattis diam vel lacus tincidunt elementum. Sed vitae adipiscing turpis. Aenean ligula nibh, molestie id viverra a, dapibus at dolor. In iaculis viverra neque, vel lacus tincidunt elementum. Sed vitae adipiscing turpis.</p>
    <a class="learn-more" href="#">OUR MISSION</a>
  </article>

  <article class="abs clinic-card" style="top:482px">
    <div class="card-side">
      <div class="side-title">LANGUAGES</div>
      <div class="languages">
        <span>English</span><span>French</span>
        <span>Spanish</span><span>Punjabi</span>
        <span>Mandarin</span><span>Tagalog</span>
      </div>
    </div>
    <h2>Languages Spoken</h2>
    <p>Donec vestibulum justo a diam ultricies pellentesque. Quisque mattis diam vel lacus tincidunt elementum. Sed vitae adipiscing turpis. Aenean ligula nibh, molestie id viverra a, dapibus at dolor. In iaculis viverra neque, vel lacus tincidunt elementum. Sed vitae adipiscing turpis.</p>
    <a class="learn-more" href="#">OUR SERVICES</a>
  </article>

  <section class="abs hours-band">
    <h3>HOURS OF OPERATION</h3>
    <div class="hours-field">Mon – Fri 8:00 – 18:00 &nbsp;·&nbsp; Sat 9:00 – 13:00 &nbsp;·&nbsp; Sun Closed</div>
    <a class="directions" href="#">GET DIRECTIONS</a>
  </section>

  <footer class="abs site-footer">
    <div class="footer-col" style="left:84px;width:190px">
      <h4><b>About</b> Clinic</h4>
      <div class="rule"></div>
      <p class="tagline">A better life. Every day.</p>
      <p>We started in 1986, with a dream to bring better care to people. Today, Harbourline is one of the most dynamic, youthful and fast growing family clinics, serving patients across the region.</p>
    </div>
    <div class="footer-col" style="left:392px;width:220px">
      <h4><b>Contact</b></h4>
      <div class="rule"></div>
      <p>Harbourline Clinic,<br>Cedar Business Park,<br>Northern Ring Road,<br>Westbrook (E), Harbour City - 400512<br>Tel.: 021 - 55501900 / 01<br>Fax: 021 - 55501902<br>Email: hello@harbourline.example</p>
    </div>
    <div class="footer-col" style="left:716px;width:190px">
      <h4><b>Our</b> Clinic</h4>
      <div class="rule"></div>
      <nav class="footer-links">
        <a href="#">Mission</a>
        <a href="#">Services</a>
        <a href="#">Clinic Policies</a>
        <a href="#">Schedules</a>
      </nav>
    </div>
  </footer>

  <div class="abs footer-base"><p>©2015 Harbourline Clinic. All rights reserved.</p></div>
</body>
</html>
```